Flyer Vacation Gift Certificate

I need to create a beautiful flyer 8.5 x 11 PDF format flyer design. <br/><br/>Instructions:<br/>The flyer will really be a gift voucher for a las vegas vacation getaway. So must have a Las Vegas Theme exciting fun<br/><br/>The voucher should have two modules that will be editable. <br/>Must have a "Compliments Of" area and also must have an "Exclusively For" area<br/><br/>Keep in mind that this flyer will be printed so keep that in mind :)<br/><br/>Here the is the content for the vacation voucher:<br/><br/>There is no doubt that Las Vegas is one of the hottest travel destinations around the world. In fact, some people would even go as far as<br/>saying that perhaps it is THE hottest place to visit. Enjoy up to 4 nights of resort/casino accommodations in exciting Las Vegas, NV. Millions of people travel to this exciting city each year to enjoy its thrills. Thanks to the business you received this certificate from, now you can enjoy exciting Las Vegas, NV too!<br/><br/>Features:<br/>*Travel 7 Days A Week<br/>*Stay Your Choice Of Nights (1-4 Nights)<br/>*Good For Two Adults & Two Children<br/>*Pay Just The Taxes & Fees<br/>*Multiple Travel Date Requests Allowed<br/>*Fully Transferable To Another Person<br/>*Just A 30 Days Advance Notice Required<br/>*You Will Have 12 Months To Complete Travel After Redemption<br/><br/>HOW CAN WE DO THIS?<br/><br/>We contract with the world leading hotel chains and resorts to help them fill their otherwise empty rooms.<br/><br/>We help fill empty rooms which the hotels, resorts and cruise lines turn into additional revenue from other areas of their property and future bookings.<br/><br/>Hotels rarely experience full occupancy, yet they remain open, providing rooms and services at fixed costs. So when hotels give out their rooms by partnering with marketing companies like us, they might miss out on the room fee, but they already didn't have that in the first place, at least now they have the opportunity to gain a customer for their in-house restaurants, room service, their casinos, an extra day stay, future bookings, etc.<br/><br/>VIEW ALL THE DETAILS OF THIS SPECIAL OFFER AND REDEEM ONLINE AT <br/>WWW.TOPAZVOUCHERDESK.COM<br/><br/>Certificate ID # 47261-38504<br/>Expires 02/29/2020<br/><br/><br/>*terms and conditions apply see website for details<br/><br/>KEEP IN MIND THE EXAMPLES I AM UPLOADING ARE SIMPLY TO SHOW YOU THAT THEY CONTAIN THE "COMPLIMENTS OF" AND "EXCLUSIVELY FOR" ELEMENTS. THESE MUST BE INCLUDED IN NEW DESIGN. PLEASE ONLY USE THE CONTENT I PROVIDED IN BRIEF, DONT USE CONTENT FROM EXAMPLES.

Target Market(s)

CONSUMERS THAT HAVE BEEN REWARDED WITH A VACATION CERTIFICATE FOR DOING BUSINESS WITH A COMPANY.

COMPANIES USE THESE AS MARKETING INCENTIVES TO ATTRACT MORE CUSTOMERS AND TO REWARD LOYALTY, ETC.

Industry/Entity Type

Travel Industry

Colors

Designer to choose colors to be used in the design.

Requirements
Must have
• I need to create a beautiful flyer 8.5 x 11 PDF format flyer design.
• Instructions:
• The flyer will really be a gift voucher for a las vegas vacation getaway. So must have a Las Vegas Theme exciting fun
• The voucher should have two modules that will be editable.
• Must have a "Compliments Of" area and also must have an "Exclusively For" area
• Keep in mind that this flyer will be printed so keep that in mind :)
• Here the is the content for the vacation voucher:
• There is no doubt that Las Vegas is one of the hottest travel destinations around the world. In fact, some people would even go as far as
• saying that perhaps it is THE hottest place to visit. Enjoy up to 4 nights of resort/casino accommodations in exciting Las Vegas, NV. Millions of people travel to this exciting city each year to enjoy its thrills. Thanks to the business you received this certificate from, now you can enjoy exciting Las Vegas, NV too!
• Features:
• *Travel 7 Days A Week
• *Stay Your Choice Of Nights (1-4 Nights)
• *Good For Two Adults & Two Children
• *Pay Just The Taxes & Fees
• *Multiple Travel Date Requests Allowed
• *Fully Transferable To Another Person
• *Just A 30 Days Advance Notice Required
• *You Will Have 12 Months To Complete Travel After Redemption
• HOW CAN WE DO THIS?
• We contract with the world leading hotel chains and resorts to help them fill their otherwise empty rooms.
• We help fill empty rooms which the hotels, resorts and cruise lines turn into additional revenue from other areas of their property and future bookings.
• Hotels rarely experience full occupancy, yet they remain open, providing rooms and services at fixed costs. So when hotels give out their rooms by partnering with marketing companies like us, they might miss out on the room fee, but they already didn't have that in the first place, at least now they have the opportunity to gain a customer for their in-house restaurants, room service, their casinos, an extra day stay, future bookings, etc.
• VIEW ALL THE DETAILS OF THIS SPECIAL OFFER AND REDEEM ONLINE AT
• WWW.TOPAZVOUCHERDESK.COM
• Certificate ID # 47261-38504
• Expires 02/29/2020
• *terms and conditions apply see website for details
• KEEP IN MIND THE EXAMPLES I AM UPLOADING ARE SIMPLY TO SHOW YOU THAT THEY CONTAIN THE "COMPLIMENTS OF" AND "EXCLUSIVELY FOR" ELEMENTS. THESE MUST BE INCLUDED IN NEW DESIGN. PLEASE ONLY USE THE CONTENT I PROVIDED IN BRIEF, DONT USE CONTENT FROM EXAMPLES.
Nice to have
• EXCITING LAS VEGAS IMAGES THAT MAKE SOMEONE WANT TO GO THERE

```html
<!DOCTYPE html>
<html lang="en">
<head>
<meta charset="utf-8">
<title>Las Vegas Vacation Getaway Gift Voucher</title>
<link rel="stylesheet" href="https://fonts.googleapis.com/css2?family=Oswald:wght@500;600&family=Open+Sans:wght@400;600;700&display=swap">
<style>
:root{
  --page-bg:#dcdcdc;
  --navy:#0b2f6e;
  --blue:#124a9e;
  --blue-light:#1e62c0;
  --gold:#d6a248;
  --gold-dark:#c48f34;
  --gold-title:#f4b84a;
  --red:#e11d25;
  --white:#ffffff;
  --ink:#1c1c1c;
  --grey-panel:#ececec;
  --grey-text:#5a5a5a;
}
*{margin:0;padding:0;box-sizing:border-box}
html,body{width:1008px;height:1200px;overflow:hidden}
body{background:var(--page-bg);font-family:"Open Sans",Arial,sans-serif;position:relative}
.voucher{position:absolute;left:54px;top:18px;width:900px;height:1164px;background:var(--grey-panel);overflow:hidden;box-shadow:0 6px 18px rgba(0,0,0,.25)}
.hero-photo{position:absolute;left:0;top:0;width:900px;height:460px;
  background:radial-gradient(ellipse at 30% 35%,#e8c3a6 0%,#c99274 22%,transparent 45%),
  linear-gradient(120deg,#3a4a7a 0%,#7a5a6a 35%,#d8c9c0 60%,#c24a3a 75%,#2c3f7a 100%)}
.blue-panel{position:absolute;left:0;top:420px;width:900px;height:440px;
  background:radial-gradient(ellipse at 30% 40%,var(--blue-light) 0%,var(--blue) 40%,var(--navy) 100%)}
.swoosh{position:absolute;left:0;top:330px;width:900px;height:140px}
.ribbon-corner{position:absolute;left:0;top:0;width:160px;height:160px;overflow:hidden}
.ribbon{position:absolute;left:-52px;top:38px;width:230px;height:40px;background:var(--red);transform:rotate(-45deg);
  color:var(--white);font-family:"Oswald",sans-serif;font-weight:500;font-size:21px;letter-spacing:.5px;text-align:center;line-height:40px}
.snapshot{position:absolute;background:var(--white);padding:10px;box-shadow:0 4px 10px rgba(0,0,0,.4)}
.snapshot .shot{width:100%;height:100%}
.snapshot-gondola{left:600px;top:150px;width:300px;height:275px;transform:rotate(8deg)}
.snapshot-gondola .shot{background:linear-gradient(160deg,#7fb2e0 0%,#d9b27a 45%,#9a5a3a 70%,#2f5f7a 100%)}
.snapshot-ride{left:508px;top:313px;width:222px;height:175px;transform:rotate(-7deg)}
.snapshot-ride .shot{background:linear-gradient(170deg,#8cc6ee 0%,#e6d8a8 40%,#e05a4a 65%,#3c8a4a 100%)}
.title{position:absolute;left:44px;top:446px;font-family:"Oswald",sans-serif;line-height:1}
.title-main{display:block;color:var(--gold-title);font-size:72px;font-weight:600;letter-spacing:1px;text-shadow:0 3px 6px rgba(0,0,0,.35)}
.title-sub{display:block;color:var(--white);font-size:38px;font-weight:500;letter-spacing:.5px;margin-top:4px}
.recipient{position:absolute;left:44px;top:580px;color:var(--white);font-size:20px;line-height:30px;white-space:nowrap}
.recipient b{font-weight:700}
.intro{position:absolute;left:44px;top:650px;width:478px;color:var(--white);font-size:12.8px;line-height:17.2px;text-align:justify}
.features{position:absolute;left:538px;top:478px;width:337px;height:376px;background:var(--gold);border-radius:0 0 14px 14px;padding:12px 14px 0 14px;color:var(--white)}
.features h2{font-family:"Open Sans",sans-serif;font-weight:700;font-size:29px;line-height:36px;margin-bottom:2px}
.features ul{list-style:none}
.features li{position:relative;padding-left:25px;font-size:14px;line-height:28.5px;border-bottom:1px solid rgba(255,255,255,.35)}
.features li:last-child{border-bottom:none;line-height:28px}
.features svg{position:absolute;left:0;top:7px;width:15px;height:15px}
.how-tab{position:absolute;left:0;top:812px;width:362px;height:44px;background:var(--gold);border-radius:0 22px 22px 0;
  color:var(--white);font-weight:700;font-size:20px;line-height:44px;padding-left:46px}
.how-list{position:absolute;left:44px;top:876px;width:820px;list-style:none;color:var(--ink);font-size:14px;line-height:18.5px}
.how-list li{position:relative;padding-left:30px;margin-bottom:10px}
.how-list svg{position:absolute;left:0;top:2px;width:15px;height:15px}
.cert{position:absolute;left:0;top:1044px;width:900px;text-align:center;color:var(--grey-text);font-size:12px;font-weight:600}
.footer-band{position:absolute;left:0;top:1092px;width:900px;height:72px;background:linear-gradient(90deg,var(--navy),var(--blue) 50%,var(--navy))}
.redeem{position:absolute;left:40px;top:1066px;width:835px;height:50px;background:var(--gold);border-radius:25px;
  display:flex;align-items:center;justify-content:center;gap:10px;color:var(--white);font-weight:700;font-size:13.5px;white-space:nowrap}
.redeem span{white-space:nowrap}
.redeem svg{width:14px;height:14px;flex:none}
.terms{position:absolute;left:0;top:1130px;width:900px;text-align:center;color:var(--white);font-size:13px}
</style>
</head>
<body>
<main class="voucher">
  <div class="hero-photo" role="img" aria-label="Smiling family of four in front of the Welcome to Fabulous Las Vegas sign"></div>
  <div class="blue-panel"></div>
  <svg class="swoosh" viewBox="0 0 900 140" preserveAspectRatio="none" aria-hidden="true">
    <path d="M0 78 Q330 0 900 16 L900 140 L0 140Z" fill="var(--white)"/>
    <path d="M0 96 Q330 22 900 34 L900 140 L0 140Z" fill="var(--gold)"/>
    <path d="M0 104 Q330 32 900 42 L900 140 L0 140Z" fill="var(--blue)"/>
  </svg>
  <div class="ribbon-corner"><div class="ribbon">GIFT VOUCHER</div></div>
  <figure class="snapshot snapshot-gondola"><div class="shot" role="img" aria-label="Couple riding a gondola along a Venetian-style canal"></div></figure>
  <figure class="snapshot snapshot-ride"><div class="shot" role="img" aria-label="Children with raised arms on an amusement park ride"></div></figure>

  <h1 class="title"><span class="title-main">LAS VEGAS</span><span class="title-sub">VACATION GETAWAY</span></h1>

  <div class="recipient">
    <p><b>COMPLIMENTS OF:</b> Two Adults &amp; Two Children</p>
    <p><b>EXCLUSIVELY FOR:</b> Customer Name</p>
  </div>

  <p class="intro">There is no doubt that Las Vegas is one of the hottest travel destinations around the world. In fact, some people would even go as far as saying that perhaps it is THE hottest place to visit. Enjoy up to 4 nights of resort/casino accommodations in exciting Las Vegas, NV. Millions of people travel to this exciting city each year to enjoy its thrills. Thanks to the business you received this certificate from, now you can enjoy exciting Las Vegas, NV too!</p>

  <section class="features">
    <h2>FEATURES:</h2>
    <ul>
      <li><svg viewBox="0 0 16 16"><circle cx="8" cy="8" r="8" fill="var(--white)"/><path d="M6.5 4.5L10 8l-3.5 3.5" fill="none" stroke="var(--gold)" stroke-width="2"/></svg>Travel 7 Days A Week</li>
      <li><svg viewBox="0 0 16 16"><circle cx="8" cy="8" r="8" fill="var(--white)"/><path d="M6.5 4.5L10 8l-3.5 3.5" fill="none" stroke="var(--gold)" stroke-width="2"/></svg>Stay Your Choice Of Nights (1- 4 Nights)</li>
      <li><svg viewBox="0 0 16 16"><circle cx="8" cy="8" r="8" fill="var(--white)"/><path d="M6.5 4.5L10 8l-3.5 3.5" fill="none" stroke="var(--gold)" stroke-width="2"/></svg>Good For Two Adults &amp; Two Children</li>
      <li><svg viewBox="0 0 16 16"><circle cx="8" cy="8" r="8" fill="var(--white)"/><path d="M6.5 4.5L10 8l-3.5 3.5" fill="none" stroke="var(--gold)" stroke-width="2"/></svg>Pay Just The Taxes &amp; Fees</li>
      <li><svg viewBox="0 0 16 16"><circle cx="8" cy="8" r="8" fill="var(--white)"/><path d="M6.5 4.5L10 8l-3.5 3.5" fill="none" stroke="var(--gold)" stroke-width="2"/></svg>Multiple Travel Date Requests Allowed</li>
      <li><svg viewBox="0 0 16 16"><circle cx="8" cy="8" r="8" fill="var(--white)"/><path d="M6.5 4.5L10 8l-3.5 3.5" fill="none" stroke="var(--gold)" stroke-width="2"/></svg>Fully Transferable To Another Person</li>
      <li><svg viewBox="0 0 16 16"><circle cx="8" cy="8" r="8" fill="var(--white)"/><path d="M6.5 4.5L10 8l-3.5 3.5" fill="none" stroke="var(--gold)" stroke-width="2"/></svg>Just A 30 Days Advance Notice Required</li>
      <li><svg viewBox="0 0 16 16"><circle cx="8" cy="8" r="8" fill="var(--white)"/><path d="M6.5 4.5L10 8l-3.5 3.5" fill="none" stroke="var(--gold)" stroke-width="2"/></svg>You Will Have 12 Months To Complete Travel After Redemption</li>
    </ul>
  </section>

  <h2 class="how-tab">HOW CAN WE DO THIS?</h2>
  <ul class="how-list">
    <li><svg viewBox="0 0 16 16"><circle cx="8" cy="8" r="7" fill="none" stroke="var(--gold-dark)" stroke-width="1.6"/><path d="M6.5 4.8L9.7 8l-3.2 3.2" fill="none" stroke="var(--gold-dark)" stroke-width="1.8"/></svg>We contract with the world leading hotel chains and resorts to help them fill their otherwise empty rooms.</li>
    <li><svg viewBox="0 0 16 16"><circle cx="8" cy="8" r="7" fill="none" stroke="var(--gold-dark)" stroke-width="1.6"/><path d="M6.5 4.8L9.7 8l-3.2 3.2" fill="none" stroke="var(--gold-dark)" stroke-width="1.8"/></svg>We help fill empty rooms which the hotels, resorts and cruise lines turn into additional revenue from other areas of their property and future bookings.</li>
    <li><svg viewBox="0 0 16 16"><circle cx="8" cy="8" r="7" fill="none" stroke="var(--gold-dark)" stroke-width="1.6"/><path d="M6.5 4.8L9.7 8l-3.2 3.2" fill="none" stroke="var(--gold-dark)" stroke-width="1.8"/></svg>Hotels rarely experience full occupancy, yet they remain open, providing rooms and services at fixed costs. So when hotels give out their rooms by partnering with marketing companies like us, they might miss out on the room fee, but they already didn't have that in the first place, at least now they have the opportunity to gain a customer for their in-house restaurants, room service, their casinos, an extra day stay, future bookings, etc.</li>
  </ul>

  <p class="cert">Certificate ID # 47261-38504 &nbsp;|&nbsp; Expires 02/29/2020</p>

  <div class="footer-band"></div>
  <p class="redeem"><span>VIEW ALL THE DETAILS OF THIS SPECIAL OFFER AND REDEEM ONLINE AT</span>
    <svg viewBox="0 0 16 16" aria-hidden="true"><circle cx="8" cy="8" r="6.5" fill="none" stroke="var(--white)" stroke-width="1.4"/><ellipse cx="8" cy="8" rx="2.8" ry="6.5" fill="none" stroke="var(--white)" stroke-width="1.2"/><path d="M1.5 8h13" stroke="var(--white)" stroke-width="1.2"/></svg>
    <span>WWW.TOPAZVOUCHERDESK.COM</span></p>
  <p class="terms">*terms and conditions apply see website for details</p>
</main>
</body>
</html>
```